Creative Report - A Presentation

We are looking for a report to visual workers' compensation claim data and the impact claims have on premium. I’m looking for something that is very visually new, appealing, easy to understand, and cutting edge.

Right now we are looking for 6 pages to be designed: a cover page, an informative page, and 4 reports. The key data for the last 3 reports are listed in the other document attached named “Key Data for Report”. These should be designed in a 8.5 x 11 page layout.

I would prefer a way where things can be combined without looking too crowded. You can play around with the background, for printing purposes try to leave white space.

Attached are a few graphs that I found that I like the look of. Please design when YOU think is best. The docx & the comments on the side are just to help you visualize.

We are a mod analysis company that is always developing new reports. We are hoping to find a designer we can work with in the future as well – think of this as a trial run!

2 designers reached out this morning wanting to submit designs, I would like to see what they have.

```html
<!DOCTYPE html>
<html lang="en">
<head>
<meta charset="utf-8">
<title>Workers Compensation Executive Summary</title>
<link rel="stylesheet" href="https://fonts.googleapis.com/css2?family=Carlito:wght@400;700&family=Mulish:wght@400;600&family=Open+Sans:wght@400;600;700&family=Source+Sans+3:wght@400;600&display=swap">
<style>
  :root {
    --backdrop: #f2f2f2;
    --paper: #ffffff;
    --sky: #0295d8;
    --teal: #0a7f9c;
    --teal-light: #0a97ba;
    --navy: #1b4b8a;
    --ink: #231f20;
    --body: #2b2b2b;
    --muted: #9a9a9a;
    --tile-1: #0a7fa0;
    --tile-2: #6fc8ee;
    --tile-3: #1a9be0;
    --tile-4: #114a88;
    --tile-5: #142f5e;
    --tile-6: #1aa8d8;
  }
  * { margin: 0; padding: 0; box-sizing: border-box; }
  html, body { width: 1200px; height: 871px; overflow: hidden; background: var(--backdrop); }
  .spread { position: relative; width: 1200px; height: 871px; }
  .page {
    position: absolute; top: 90px; width: 535px; height: 692px;
    background: var(--paper); overflow: hidden;
    box-shadow: 0 3px 10px rgba(0,0,0,0.18);
  }
  .cover { left: 53px; }
  .summary { left: 619px; }

  /* Cover */
  .cover-art { position: absolute; inset: 0; width: 535px; height: 692px; }
  .cover-logo {
    position: absolute; left: 92px; top: 58px;
    font-family: "Source Sans 3", sans-serif; font-weight: 400;
    font-size: 33px; color: #fff; letter-spacing: 0.5px;
  }
  .agent {
    position: absolute; left: 25px; top: 264px; color: #fff;
    font-family: "Source Sans 3", sans-serif;
  }
  .agent-heading { font-size: 16.5px; font-weight: 600; line-height: 22px; }
  .agent-line { font-size: 16px; line-height: 21px; }
  .cover-title {
    position: absolute; right: 25px; top: 140px; text-align: right;
    font-family: "Open Sans", sans-serif; color: var(--ink);
    font-size: 40px; line-height: 42px; letter-spacing: -0.5px;
  }
  .cover-title .strong { font-weight: 700; }
  .cover-rule {
    position: absolute; left: 329px; top: 330px; width: 182px; height: 2px; background: var(--navy);
  }
  .mod-effective {
    position: absolute; right: 27px; top: 347px; text-align: right;
    font-family: "Open Sans", sans-serif; color: var(--navy);
  }
  .mod-label { font-size: 28px; font-weight: 600; line-height: 34px; letter-spacing: -0.3px; }
  .mod-date { font-size: 28px; font-weight: 400; line-height: 34px; }

  /* Summary page */
  .summary-body {
    position: absolute; left: 24px; top: 35px; width: 487px;
    font-family: "Mulish", sans-serif; font-size: 10.4px; line-height: 13.2px; color: var(--body);
    text-align: justify;
  }
  .summary-body p { margin-bottom: 0; }
  .term { color: var(--navy); font-weight: 600; }
  .lead-in { margin-top: 13px; }
  .cost-icons {
    display: flex; gap: 15.5px; margin-top: 20px; list-style: none; text-align: center;
  }
  .cost-icon { width: 64px; }
  .cost-icon .tile { display: block; width: 64px; height: 65px; border-radius: 5px; }
  .cost-icon .label { display: block; margin-top: 12px; font-size: 7px; line-height: 9px; }
  .tile-1 { background: var(--tile-1); } .tile-2 { background: var(--tile-2); }
  .tile-3 { background: var(--tile-3); } .tile-4 { background: var(--tile-4); }
  .tile-5 { background: var(--tile-5); } .tile-6 { background: var(--tile-6); }
  .osha-note {
    margin-top: 24px; font-family: "Carlito", sans-serif; font-size: 16.5px; line-height: 21px;
    color: var(--ink); text-align: left;
  }
  .osha-note strong { font-weight: 700; }
  .body-block { margin-top: 17px; }
  .mod-factors { list-style: none; margin: 16px 0 0 0; }
  .mod-factors li { position: relative; padding-left: 18px; margin-bottom: 8.5px; }
  .mod-factors li::before {
    content: ""; position: absolute; left: 6px; top: 4px; width: 5px; height: 5px;
    border-radius: 50%; background: var(--ink);
  }
  .spaced { margin-top: 13px; }
  .summary-footer {
    position: absolute; left: 24px; top: 644px; width: 425px; padding-top: 8px;
    border-top: 1px solid #555;
    font-family: "Mulish", sans-serif; font-size: 7.4px; line-height: 9.6px; color: var(--body);
  }
  .footer-logo {
    position: absolute; left: 460px; top: 651px;
    font-family: "Mulish", sans-serif; font-weight: 600; font-size: 12px; color: var(--muted);
  }
</style>
</head>
<body>
<main class="spread">

  <section class="page cover">
    <svg class="cover-art" viewBox="0 0 1010 1307" preserveAspectRatio="none" aria-hidden="false">
      <defs>
        <linearGradient id="tealBlend" x1="0" y1="0" x2="0.6" y2="1">
          <stop offset="0" stop-color="#0a7590"/>
          <stop offset="0.5" stop-color="#0a86a6"/>
          <stop offset="1" stop-color="#0a9bc2"/>
        </linearGradient>
        <linearGradient id="photoTones" x1="0" y1="0" x2="1" y2="1">
          <stop offset="0" stop-color="#2a8fc4"/>
          <stop offset="0.45" stop-color="#3db5b0"/>
          <stop offset="0.75" stop-color="#b83a3a"/>
          <stop offset="1" stop-color="#1fa0d6"/>
        </linearGradient>
      </defs>
      <path d="M22 0 H695 L378 318 Q346 350 314 318 L22 26 Z" fill="#0295d8"/>
      <path d="M0 36 L385 420 Q400 435 420 440 Q470 455 545 560 Q580 600 545 640 L410 760 L0 1168 Z" fill="url(#tealBlend)"/>
      <g role="img" aria-label="Photo of a gloved hand holding wooden blocks labelled compensation with worker, justice and money icons">
        <path d="M0 1190 L440 750 Q470 730 500 760 L980 1260 Q1010 1307 960 1307 H0 Z" fill="url(#photoTones)"/>
      </g>
      <path d="M549 804 L900 1194" stroke="#1b4b8a" stroke-width="7"/>
    </svg>

    <div class="cover-logo">LOGO HERE</div>

    <div class="agent">
      <p class="agent-heading">AGENT INFORMATION</p>
      <p class="agent-line">Name of agent</p>
      <p class="agent-line">Phone #</p>
      <p class="agent-line">Email</p>
    </div>

    <h1 class="cover-title">
      <span class="strong">WORKERS</span><br>
      <span class="strong">COMPENSATION</span><br>
      EXECUTIVE<br>
      SUMMARY
    </h1>
    <div class="cover-rule"></div>
    <div class="mod-effective">
      <p class="mod-label">Mod Effective</p>
      <p class="mod-date">10-08-2022</p>
    </div>
  </section>

  <section class="page summary">
    <div class="summary-body">
      <p><span class="term">Workers compensation</span>&nbsp; claims can have a significant impact on a business. In addition to the direct claim costs, there are many other costs associated with a workers compensation claim that can impact a business.</p>
      <p class="lead-in">They are:</p>

      <ul class="cost-icons">
        <li class="cost-icon"><span class="tile tile-1" role="img" aria-label="Icon of a head with dollar sign and brick wall"></span><span class="label">Work Comp<br>Premium Costs</span></li>
        <li class="cost-icon"><span class="tile tile-2" role="img" aria-label="Icon of a person working at a laptop at night"></span><span class="label">Overtime</span></li>
        <li class="cost-icon"><span class="tile tile-3" role="img" aria-label="Icon of a person inside a gear"></span><span class="label">Administrative time spent on claim after an injury</span></li>
        <li class="cost-icon"><span class="tile tile-4" role="img" aria-label="Icon of a person with arrows pointing outward"></span><span class="label">Lost Opportunities due to staffing</span></li>
        <li class="cost-icon"><span class="tile tile-5" role="img" aria-label="Icon of a bar chart with circular arrows and a clock"></span><span class="label">Lost Productivity</span></li>
        <li class="cost-icon"><span class="tile tile-6" role="img" aria-label="Icon of a hand holding a wrench inside a gear"></span><span class="label">Clean up or repair of damaged equipment</span></li>
      </ul>

      <p class="osha-note"><strong>OSHA</strong> estimates that depending upon the size of the claim indirect costs range from 1 to 4 times the direct costs.</p>

      <p class="body-block">The following report explains in detail how a workers compensation claim affects the premium that your business pays for workers compensation. Most business have an experience mod that is reflective of their past claims experience and every claim has an impact on the experience mod. It is important to note that some claims affect the mod differently.</p>

      <ul class="mod-factors">
        <li>A medical only claim is reduced by 70% in the mod calculation.</li>
        <li>A medical/indemnity claim has no reduction.</li>
        <li>All claims are also limited by a primary threshold value where claims are grouped into primary claims and excess claims.</li>
      </ul>

      <p class="spaced" style="margin-top:16px">The following report will analyze the types of claims that are occurring in your business and will group them together for ease of identifying trends and areas of opportunity to improve.</p>
      <p class="spaced">By identifying the types and causes of losses many times a cost/benefit analysis can be performed to allow for safety training, additional equipment or building or process improvements.</p>
      <p class="spaced">For the premium cost analysis in this report we have used a manual premium of $XXX,XXX. A manual premium is the premium derived by the carrier before any credits, debits, or experience rating.</p>
    </div>

    <footer class="summary-footer">
      Proprietary and Confidential. Premium Lens provides for an ESTIMATE of an experience modification factor. Your official experience modification factor is issued solely by the applicable workers' compensation rating bureau. Premium Lens Inc. All Rights Reserved.
    </footer>
    <div class="footer-logo">LOGO</div>
  </section>

</main>
</body>
</html>
```